Property Finance Company - Orin Ventures Limited

Background: Orin Ventures Group Limited is a private property finance company. Orin Ventures Group has capital to directly fund first mortgage, mezzanine and preferred equity financing. We also acquire performing, sub-performing and distressed debt.

Orin Ventures' management philosophy emphasises expertise, innovation, wisdom, honesty and competitiveness. Orin Ventures are not finance brokers - we provide debt funding to the commercial property and residential development sectors. Our process is built from experience and cumutavely Orin Ventures' Directors have in excess of 60 years wisdom.

The aim of the website will be to increase brand awareness, provide clients with comfort around our level of skill and background on who we are, generate more sales, and provide examples of projects that we have funded.

The website is a new product launch, and we need to use our Orin Ventures logo that has just been designed. We like a dark background, and either black/silver/grey/ jade green, or black/gold/jade green colours.

Our unique advantages are that we have fast turnaround times, we can solve clients funding problems and we know what we are doing. Our target audience will be viewing the website on both desktop and mobile devices.

We would like to have the following pages:

Home
About
Team
Services
Project Experience
Contact

Competitors Website: http://www.tarvelo.com/

We would also like to have the option of video footage in our website, as you can see in our competitors website.

Overall we want a really slick, elegant but modern website that is better than www.tarvelo.com

Target Market(s)

Finance borrowers, property developers, accountants, lawyers, businesspeople, high net worth people

Industry/Entity Type

Finance

Requirements
Must have
• Please see project description
Nice to have
Should not have

```html
<!DOCTYPE html>
<html lang="en">
<head>
<meta charset="utf-8">
<title>Orin Ventures Group</title>
<link href="https://fonts.googleapis.com/css2?family=Open+Sans:wght@400;600;700&display=swap" rel="stylesheet">
<style>
:root{
  --black:#0e0e0e;
  --dark:#161616;
  --panel:#1c1c1c;
  --grey-band:#2a2a2a;
  --gold:#f2b31b;
  --gold-dark:#d99a0c;
  --jade:#1f8a3c;
  --white:#ffffff;
  --text-light:#b9b9b9;
  --text-dim:#8a8a8a;
  --text-dark:#444444;
  --hero-a:#8a6a52;
  --hero-b:#d7cfc4;
}
*{box-sizing:border-box;margin:0;padding:0}
html,body{width:750px;height:1200px;overflow:hidden}
body{background:var(--black);font-family:'Open Sans',Arial,sans-serif;color:var(--white);position:relative}

/* header */
.site-header{position:absolute;top:0;left:0;width:750px;height:32px;background:var(--dark);border-bottom:3px solid var(--gold);display:flex;align-items:center;padding:0 28px 0 112px}
.brand{display:flex;align-items:center;gap:6px;font-weight:700;font-size:10px;letter-spacing:.5px;color:var(--white)}
.brand-dot{width:14px;height:14px;border-radius:50%;background:var(--gold)}
.main-nav{display:flex;gap:14px;margin-left:auto;font-size:7px;font-weight:600;letter-spacing:.3px}
.main-nav a{color:var(--white);text-decoration:none}
.main-nav a.active{color:var(--gold)}
.header-contact{display:flex;align-items:center;gap:4px;margin-left:40px;font-size:7px;color:var(--white)}
.apply-btn{margin-left:12px;background:var(--gold);color:var(--black);font-size:6.5px;font-weight:700;padding:3px 8px;border-radius:2px}

/* hero */
.hero{position:absolute;top:35px;left:0;width:750px;height:327px;background:linear-gradient(100deg,var(--hero-a) 0%,var(--hero-b) 45%,#b89c83 70%,#6d5444 100%)}
.watch-video{position:absolute;right:120px;bottom:30px;display:flex;align-items:center;gap:5px;font-size:7px;font-weight:600;color:var(--white)}
.hero-dots{position:absolute;bottom:10px;left:50%;transform:translateX(-50%);display:flex;gap:5px}
.hero-dots span{width:6px;height:6px;border-radius:50%;background:rgba(255,255,255,.55)}
.hero-dots span.on{background:var(--gold)}

/* services */
.services{position:absolute;top:398px;left:112px;width:530px;display:flex;gap:10px}
.service-card{flex:1;height:95px;background:var(--jade);border-radius:3px;padding:8px 9px;position:relative}
.service-card h3{font-size:10px;color:var(--gold);font-weight:700;margin-bottom:4px}
.service-card p{font-size:6.5px;line-height:1.4;color:var(--white);width:88px}
.service-thumb{position:absolute;right:9px;top:14px;width:66px;height:66px;border-radius:50%;border:3px solid var(--gold);background:linear-gradient(160deg,#d8dde2,#7d8791)}
.btn{display:inline-block;background:var(--gold);color:var(--black);font-size:6px;font-weight:700;padding:3px 8px;border-radius:9px}
.service-card .btn{position:absolute;left:9px;bottom:9px}

/* welcome */
.welcome{position:absolute;top:515px;left:112px;width:530px;height:230px;display:flex;gap:28px}
.welcome-mark{width:150px;display:flex;flex-direction:column;align-items:center;justify-content:center;gap:10px}
.welcome-mark .mark-circle{width:90px;height:90px;border-radius:50%;background:#2d2d2d}
.welcome-mark span{font-size:13px;font-weight:700;color:#5a5a5a;letter-spacing:1px}
.welcome-text{flex:1;padding-top:40px}
.welcome-text h1{font-size:17px;font-weight:400;margin-bottom:10px}
.welcome-text h1 strong{color:var(--gold);font-weight:700}
.welcome-text p{font-size:7px;line-height:1.6;color:var(--text-light);margin-bottom:8px}

/* feature band */
.feature-band{position:absolute;top:775px;left:0;width:750px;height:245px;background:var(--grey-band);border-top:1px solid #333}
.feature-cards{position:absolute;top:20px;left:112px;width:530px;display:flex;gap:18px}
.feature-card{flex:1;height:200px;background:var(--white);border-radius:3px;position:relative;overflow:hidden;padding:12px 12px}
.feature-card h2{font-size:10px;color:var(--gold-dark);font-weight:600;margin-bottom:8px}
.why-list{list-style:none;font-size:6.5px;color:var(--text-dark);line-height:2}
.why-list li{display:flex;align-items:center;gap:4px}
.why-list svg{flex:none}
.feature-card .btn{position:absolute;left:12px;bottom:14px}
.person-photo{position:absolute;right:0;bottom:0;width:110px;height:180px;background:linear-gradient(180deg,#eeeeee,#7ea4c4)}
.quote{font-size:6.5px;line-height:1.6;color:var(--text-dark);width:135px;display:flex;gap:4px}
.quote .qmark{color:var(--gold-dark);font-size:14px;line-height:1;font-weight:700}
.quote-name{font-size:7.5px;font-weight:700;color:#222;margin:10px 0 0 12px}
.quote-dots{position:absolute;left:24px;bottom:16px;display:flex;gap:4px}
.quote-dots span{width:5px;height:5px;border-radius:50%;background:#cccccc}
.quote-dots span.on{background:#555}
.customer-photo{position:absolute;right:0;bottom:0;width:105px;height:170px;background:linear-gradient(180deg,#f2efea,#d9c7b5)}

/* footer */
.site-footer{position:absolute;top:1022px;left:0;width:750px;height:153px;background:var(--dark);border-top:3px solid var(--gold);padding:14px 112px 0;display:flex;gap:24px}
.footer-col h4{font-size:8px;font-weight:600;margin-bottom:8px}
.footer-col p,.footer-col li{font-size:6.5px;color:var(--text-light);line-height:1.6;list-style:none}
.newsletter{width:150px}
.signup{display:flex;margin-bottom:8px}
.signup span{background:var(--white);color:var(--text-dim);font-size:6px;padding:4px 5px;width:90px}
.signup b{background:var(--gold);color:var(--black);font-size:6px;padding:4px 6px}
.social{display:flex;gap:4px}
.social i{width:12px;height:12px;border-radius:50%;border:1px solid var(--text-light);display:block}
.contact-col{width:120px}
.links-col{width:100px}
.footer-mark{margin-left:auto;display:flex;flex-direction:column;align-items:center;gap:6px;padding-top:6px}
.footer-mark .mark-circle{width:44px;height:44px;border-radius:50%;background:#2d2d2d}
.footer-mark span{font-size:8px;font-weight:700;color:#5a5a5a}
.copyright{position:absolute;top:1175px;left:0;width:750px;height:25px;background:var(--black);font-size:6.5px;color:var(--text-dim);text-align:center;line-height:25px}
</style>
</head>
<body>

<header class="site-header">
  <div class="brand"><span class="brand-dot"></span>ORIN VENTURES GROUP</div>
  <nav class="main-nav">
    <a class="active" href="#">HOME</a><a href="#">ABOUT</a><a href="#">TEAM</a><a href="#">SERVICES</a><a href="#">PROJECT EXPERIENCE</a><a href="#">CONTACT</a>
  </nav>
  <div class="header-contact">
    <svg width="8" height="8" viewBox="0 0 10 10"><path d="M2 1l2 2-1 1.5c.7 1.3 1.5 2.1 2.5 2.5L7 6l2 2-1.5 1.5C4.5 9 1 5.5.5 2.5z" fill="#f2b31b"/></svg>
    (0800) 431 2290
  </div>
  <span class="apply-btn">APPLY</span>
</header>

<section class="hero" role="img" aria-label="Photo of a smiling business team gathered around a table with a laptop">
  <div class="watch-video">
    <svg width="14" height="14" viewBox="0 0 14 14"><circle cx="7" cy="7" r="6.3" fill="none" stroke="#fff" stroke-width="1"/><path d="M5.5 4.5l4 2.5-4 2.5z" fill="#fff"/></svg>
    WATCH VIDEO
  </div>
  <div class="hero-dots"><span class="on"></span><span></span><span></span></div>
</section>

<section class="services">
  <article class="service-card">
    <h3>Orin Services</h3>
    <p>We directly fund first mortgage, mezzanine and equity finance.</p>
    <div class="service-thumb" role="img" aria-label="Photo of a modern office building"></div>
    <span class="btn">READ MORE</span>
  </article>
  <article class="service-card">
    <h3>Orin Team</h3>
    <p>Directors with over sixty years of property finance wisdom.</p>
    <div class="service-thumb" role="img" aria-label="Photo of a city street with towers"></div>
    <span class="btn">READ MORE</span>
  </article>
  <article class="service-card">
    <h3>Orin Project</h3>
    <p>See examples of the developments and projects we have funded.</p>
    <div class="service-thumb" role="img" aria-label="Photo of a tall residential tower"></div>
    <span class="btn">READ MORE</span>
  </article>
</section>

<section class="welcome">
  <div class="welcome-mark"><div class="mark-circle"></div><span>ORIN VENTURES</span></div>
  <div class="welcome-text">
    <h1>Welcome to <strong>Orin Ventures Group</strong></h1>
    <p>Orin Ventures Group is a private property finance company with capital to directly fund first mortgage, mezzanine and preferred equity financing. We also acquire performing, sub-performing and distressed debt. We are not finance brokers; we provide debt funding to the commercial property and residential development sectors across the country.</p>
    <p>Our process is built from experience. We offer fast turnaround times, we solve funding problems for our clients and we know what we are doing.</p>
    <span class="btn">READ MORE</span>
  </div>
</section>

<section class="feature-band">
  <div class="feature-cards">
    <article class="feature-card">
      <h2>Why Choose Us</h2>
      <ul class="why-list">
        <li><svg width="6" height="6" viewBox="0 0 6 6"><path d="M1 3l1.5 1.5L5 1.5" stroke="#d99a0c" fill="none"/></svg>Fast turnaround times</li>
        <li><svg width="6" height="6" viewBox="0 0 6 6"><path d="M1 3l1.5 1.5L5 1.5" stroke="#d99a0c" fill="none"/></svg>Direct funding, no brokers</li>
        <li><svg width="6" height="6" viewBox="0 0 6 6"><path d="M1 3l1.5 1.5L5 1.5" stroke="#d99a0c" fill="none"/></svg>Over 60 years of wisdom</li>
        <li><svg width="6" height="6" viewBox="0 0 6 6"><path d="M1 3l1.5 1.5L5 1.5" stroke="#d99a0c" fill="none"/></svg>First mortgage lending</li>
        <li><svg width="6" height="6" viewBox="0 0 6 6"><path d="M1 3l1.5 1.5L5 1.5" stroke="#d99a0c" fill="none"/></svg>Mezzanine finance options</li>
        <li><svg width="6" height="6" viewBox="0 0 6 6"><path d="M1 3l1.5 1.5L5 1.5" stroke="#d99a0c" fill="none"/></svg>Preferred equity financing</li>
        <li><svg width="6" height="6" viewBox="0 0 6 6"><path d="M1 3l1.5 1.5L5 1.5" stroke="#d99a0c" fill="none"/></svg>Distressed debt acquisition</li>
        <li><svg width="6" height="6" viewBox="0 0 6 6"><path d="M1 3l1.5 1.5L5 1.5" stroke="#d99a0c" fill="none"/></svg>Honest, competitive terms</li>
      </ul>
      <span class="btn">READ MORE</span>
      <div class="person-photo" role="img" aria-label="Photo of a businessman in a blue shirt pointing to the list"></div>
    </article>
    <article class="feature-card">
      <h2>Happy Customers</h2>
      <div class="quote"><span class="qmark">&ldquo;</span><span>Orin Ventures solved our funding problem within days. Their team was honest, quick and knew exactly what our development needed. We would gladly work with them again.</span></div>
      <p class="quote-name">Marisa</p>
      <div class="quote-dots"><span class="on"></span><span></span><span></span><span></span></div>
      <div class="customer-photo" role="img" aria-label="Photo of a smiling customer in a white top"></div>
    </article>
  </div>
</section>

<footer class="site-footer">
  <div class="footer-col newsletter">
    <h4>Sign up for Newsletter</h4>
    <div class="signup"><span>Email Address</span><b>GO</b></div>
    <div class="social"><i></i><i></i><i></i><i></i></div>
  </div>
  <div class="footer-col contact-col">
    <h4>Contact Info</h4>
    <p>Orin Ventures Group<br>88 Harbour Street<br>Auckland 1010<br><br>T: 0800 431 2290<br>Email Us</p>
  </div>
  <div class="footer-col links-col">
    <h4>Quick Links</h4>
    <ul><li>Home</li><li>About</li><li>Team</li><li>Services</li><li>Project Experience</li><li>Contact</li></ul>
  </div>
  <div class="footer-mark"><div class="mark-circle"></div><span>ORIN VENTURES</span></div>
</footer>

<div class="copyright">Copyright &copy; 2016 Orin Ventures Group. All Rights Reserved</div>

</body>
</html>
```